Redesign wellness clinic website

The project is redesign a wellness clinic http://www.thornleighvitality.example. The new website is to be responsive,clean,bright and a strong call to action which is to book an appointment. The logo will remain the same but the colour scheme on the website should be reflect purple white and green. I want it to be bright and cheerful and the feeling of clarity. The website shouldn't be overloaded with content but more visuals.

Target Market(s)

Anyone that has corporate wellness benefits within the downtown Toronto core. Majority of audience are professional working in Media, Telecommunications and Investments.

Industry/Entity Type

Health And Wellness

Number of Pages Required

5+ page

Font styles to use
Sans Serif

Colors
ffffff
886aae
acd036

Requirements
Must have
• -Strong call to action which is book an appointment like this page https://www.kestrelmotion.example/
• -Services provided icons on the page like https://www.brightpathvitalityhouse.example/
• - Pictures of a good visualizing a fit and healthy life
• - Strong ratings from Quorva, Zintrel, PostMaz, similar to this website http://www.summitbalancehealth.example/our-team-professionals/
• - Bright and clear
Should not have
• -No black and white images (redo our pictures)
• -Dark themes

```html
<!DOCTYPE html>
<html lang="en">
<head>
<meta charset="utf-8">
<title>Thornleigh Vitality Centre</title>
<link href="https://fonts.googleapis.com/css2?family=Open+Sans:wght@400;600;700;800&display=swap" rel="stylesheet">
<style>
:root{
  --purple:#8b3f9d;
  --purple-dark:#6e2a80;
  --purple-soft:#886aae;
  --green:#acd036;
  --green-dark:#97b92a;
  --white:#ffffff;
  --ink:#333333;
  --grey:#777777;
  --line:#e4e4e4;
}
*{box-sizing:border-box;margin:0;padding:0}
html,body{width:1200px;height:2620px;overflow:hidden}
body{font-family:"Open Sans",Arial,sans-serif;color:var(--ink);background:var(--white);position:relative}
section,header,footer{position:absolute;left:0;width:1200px}
.abs{position:absolute}

/* header */
.site-header{top:0;height:72px;background:var(--white);border-bottom:3px solid var(--purple)}
.brand{left:215px;top:13px;display:flex;align-items:center;gap:8px}
.brand-dot{width:42px;height:42px;border-radius:50%;background:var(--purple);flex:none}
.brand-name{font-size:13px;font-weight:700;color:var(--purple);line-height:1.2;white-space:nowrap}
.brand-call{font-size:12px;font-weight:700;color:var(--green-dark);white-space:nowrap}
.main-nav{left:494px;top:30px;display:flex;gap:14px;font-size:10px;font-weight:600;text-transform:uppercase;color:#444;white-space:nowrap}

/* hero */
.hero{top:72px;height:366px;background:linear-gradient(100deg,#e9e5e1 0%,#d9cfc6 40%,#c9bfb9 60%,#efeeee 100%)}
.hero-title{top:128px;width:100%;text-align:center;color:var(--white);font-size:44px;font-weight:800;letter-spacing:1px;text-shadow:0 2px 6px rgba(0,0,0,.25)}
.hero-sub{top:186px;width:100%;text-align:center;color:var(--white);font-size:13px;font-weight:600;text-transform:uppercase}
.slide-arrow{top:152px;width:34px;height:34px;border:1px solid rgba(255,255,255,.8)}
.btn-slant{display:flex;align-items:center;justify-content:center;font-weight:700;text-transform:uppercase;clip-path:polygon(5% 0,100% 0,95% 100%,0 100%)}
.btn-book{background:var(--green);color:var(--white);font-size:19px}
.hero .btn-book{left:448px;top:240px;width:304px;height:44px}
.hero-chevron{left:588px;top:322px}

/* welcome */
.welcome{top:438px;height:327px;background:var(--white)}
.welcome-photo{left:640px;top:0;width:560px;height:327px;background:linear-gradient(90deg,#ffffff 0%,#e6f0ec 35%,#cfe3d9 70%,#dde8e2 100%)}
.welcome-small{top:50px;left:0;width:1256px;text-align:center;font-size:21px;font-weight:800;color:#222}
.welcome-title{top:76px;left:0;width:1256px;text-align:center;font-size:30px;font-weight:700;color:var(--purple)}
.welcome-text{top:142px;left:318px;width:620px;text-align:center;font-size:14px;line-height:1.6;color:#444}
.btn-outline{left:567px;top:226px;width:90px;height:30px;border:1px solid var(--purple);color:var(--purple);font-size:9px;font-weight:700;display:flex;align-items:center;justify-content:center;text-transform:uppercase}

/* services */
.services{top:765px;height:422px;background:linear-gradient(120deg,var(--purple) 0%,#9b52ae 55%,var(--purple-dark) 100%)}
.section-title-light{top:40px;width:100%;text-align:center;color:var(--white);font-size:24px;font-weight:700;text-transform:uppercase}
.service{top:128px;width:118px;height:110px;background:rgba(80,20,95,.35);text-align:center}
.service-icon{width:84px;height:84px;border-radius:50%;background:var(--white);margin:-14px auto 0;border:4px solid rgba(255,255,255,.5);background-clip:padding-box}
.service-label{color:var(--white);font-size:13px;font-weight:600;margin-top:8px;line-height:1.2}
.services .btn-book{left:448px;top:330px;width:304px;height:44px}

/* updates */
.updates{top:1187px;height:363px;background:linear-gradient(90deg,#f1f1f1,#e6e6e6 50%,#f3f3f3)}
.updates-title{left:215px;top:36px;font-size:17px;font-weight:700;color:#222;text-transform:uppercase}
.see-all{left:836px;top:40px;font-size:10px;color:var(--purple)}
.pager{top:32px;width:28px;height:28px;border:1px solid var(--purple);background:var(--white)}
.card{top:91px;width:238px;height:228px;background:var(--white);box-shadow:0 2px 8px rgba(0,0,0,.12);padding:10px}
.card-img{height:80px;margin-bottom:12px}
.card-title{font-size:12px;font-weight:700;color:#333;white-space:nowrap}
.card-date{font-size:9px;color:var(--green-dark);margin:4px 0}
.card-text{font-size:10px;line-height:1.5;color:var(--grey)}
.card-more{font-size:9px;color:var(--purple);font-weight:700;margin-top:14px;text-transform:uppercase}

/* testimonials */
.testimonials{top:1550px;height:553px;background:var(--white)}
.section-title-dark{top:52px;width:100%;text-align:center;font-size:20px;font-weight:800;color:#222;text-transform:uppercase}
.section-sub{top:88px;width:100%;text-align:center;font-size:11px;color:var(--grey);line-height:1.6}
.section-link{top:136px;width:100%;text-align:center;font-size:10px;color:var(--green-dark)}
.quote-box{left:254px;top:171px;width:715px;height:179px;background:var(--purple)}
.quote-photo{left:272px;top:200px;width:148px;height:162px;background:var(--white);padding:10px;box-shadow:0 2px 8px rgba(0,0,0,.15)}
.quote-photo div{width:100%;height:100%;background:linear-gradient(135deg,#e6e6e6,#bdbdbd)}
.quote-text{left:440px;top:190px;width:505px;font-size:12px;line-height:1.55;color:var(--white);text-align:justify}
.quote-sign{left:440px;top:328px;width:505px;text-align:right;font-size:11px;font-weight:700;color:var(--white)}
.quote-nav{top:146px;width:20px;height:20px;background:var(--white);border:1px solid var(--line)}
.rating{top:388px;width:178px;height:119px;background:var(--white);border:1px solid var(--line);box-shadow:0 1px 4px rgba(0,0,0,.08);display:flex;align-items:center;justify-content:center}

/* call to action */
.cta{top:2103px;height:249px;background:linear-gradient(100deg,#b7d63f,var(--green) 50%,#9fc22c)}
.cta-title{left:210px;top:64px;color:var(--white);font-size:24px;font-weight:800;text-transform:uppercase}
.cta-line{left:210px;top:110px;color:var(--white);font-size:14px}
.cta-line b{color:#2d2d2d;text-decoration:underline}
.cta-phone{left:210px;top:140px;color:var(--white);font-size:14px}
.cta-phone strong{font-size:30px;font-weight:800;margin-right:6px}
.btn-white{background:var(--white);color:var(--purple);font-size:15px}
.cta .btn-book-alt{left:703px;top:85px;width:272px;height:42px}
.cta .btn-ask{left:703px;top:150px;width:262px;height:40px;font-size:13px}

/* footer */
.site-footer{top:2352px;height:268px;background:var(--purple);color:var(--white)}
.foot-col{top:40px}
.foot-col h4{font-size:12px;font-weight:700;text-transform:uppercase;margin-bottom:10px}
.foot-col p{font-size:10px;line-height:1.65;opacity:.9}
.foot-rule{left:210px;top:198px;width:780px;height:1px;background:rgba(255,255,255,.35)}
.social{left:220px;top:222px;display:flex;align-items:center;gap:8px;font-size:10px}
.social span.dot{width:20px;height:20px;border-radius:50%;background:rgba(255,255,255,.9)}
.foot-brand{left:800px;top:216px;display:flex;align-items:center;gap:8px;font-size:13px;font-weight:700}
.foot-brand span{width:26px;height:26px;border-radius:50%;background:var(--white)}
</style>
</head>
<body>

<header class="site-header">
  <div class="brand abs">
    <span class="brand-dot"></span>
    <div><div class="brand-name">Thornleigh Vitality Centre</div><div class="brand-call">Call 555-014-2290</div></div>
  </div>
  <nav class="main-nav abs">
    <span>Home</span><span>Fees and Services ▾</span><span>Our Staff</span><span>News &amp; Updates</span><span>Corporate Wellness</span><span>Forms</span><span>Contact</span>
  </nav>
</header>

<section class="hero" role="img" aria-label="Physiotherapist treating the back of a patient lying on a treatment table">
  <svg class="slide-arrow abs" style="left:212px" viewBox="0 0 34 34"><path d="M20 10l-7 7 7 7" fill="none" stroke="#fff" stroke-width="2"/></svg>
  <svg class="slide-arrow abs" style="left:954px" viewBox="0 0 34 34"><path d="M14 10l7 7-7 7" fill="none" stroke="#fff" stroke-width="2"/></svg>
  <h1 class="hero-title abs">PHYSIOTHERAPY</h1>
  <p class="hero-sub abs">Get your recovery on track</p>
  <div class="btn-slant btn-book abs">Book an Appointment</div>
  <svg class="hero-chevron abs" width="24" height="16" viewBox="0 0 24 16"><path d="M3 3l9 9 9-9" fill="none" stroke="#fff" stroke-width="3"/></svg>
</section>

<section class="welcome">
  <div class="welcome-photo abs" role="img" aria-label="Therapist in a green top helping a client stretch in a bright clinic"></div>
  <h2 class="welcome-small abs">WELCOME TO</h2>
  <h2 class="welcome-title abs">THORNLEIGH VITALITY CENTRE</h2>
  <p class="welcome-text abs">Established in 1989 the Thornleigh Vitality Centre has become one of Canada's leaders in providing quality care and innovative wellness programs for the community.</p>
  <div class="btn-outline abs">Explore More</div>
</section>

<section class="services">
  <h2 class="section-title-light abs">Our Services What We Do</h2>
  <div class="service abs" style="left:206px"><div class="service-icon" role="img" aria-label="Spine icon"></div><div class="service-label">Chiropractic</div></div>
  <div class="service abs" style="left:342px"><div class="service-icon" role="img" aria-label="Treatment table icon"></div><div class="service-label">Physiotherapy</div></div>
  <div class="service abs" style="left:475px"><div class="service-icon" role="img" aria-label="Exercise icon"></div><div class="service-label">Active<br>Rehabilitation</div></div>
  <div class="service abs" style="left:606px"><div class="service-icon" role="img" aria-label="Massage icon"></div><div class="service-label">Massage<br>Therapy</div></div>
  <div class="service abs" style="left:740px"><div class="service-icon" role="img" aria-label="Foot icon"></div><div class="service-label">Chiropody</div></div>
  <div class="service abs" style="left:874px"><div class="service-icon" role="img" aria-label="Body icon"></div><div class="service-label">Osteopathy</div></div>
  <div class="btn-slant btn-book abs">Book an Appointment</div>
</section>

<section class="updates">
  <h2 class="updates-title abs">Latest Updates</h2>
  <span class="see-all abs">Click here to see all</span>
  <svg class="pager abs" style="left:928px" viewBox="0 0 28 28"><path d="M16 9l-5 5 5 5" fill="none" stroke="#8b3f9d" stroke-width="2"/></svg>
  <svg class="pager abs" style="left:958px" viewBox="0 0 28 28"><path d="M12 9l5 5-5 5" fill="none" stroke="#8b3f9d" stroke-width="2"/></svg>
  <article class="card abs" style="left:215px">
    <div class="card-img" role="img" aria-label="Spa stones and bamboo" style="background:linear-gradient(135deg,#e9efe0,#b9c99a)"></div>
    <h3 class="card-title">Sed condimentum tempus eros,</h3>
    <p class="card-date">20 November 2017</p>
    <p class="card-text">It is a long established fact that a reader will be distracted by the readable content of a page...</p>
    <p class="card-more">Read More</p>
  </article>
  <article class="card abs" style="left:482px">
    <div class="card-img" role="img" aria-label="Therapist treating a knee" style="background:linear-gradient(135deg,#f3e6dc,#d8b9a4)"></div>
    <h3 class="card-title">Sed condimentum tempus eros,</h3>
    <p class="card-date">22 November 2017</p>
    <p class="card-text">It is a long established fact that a reader will be distracted by the readable content of a page...</p>
    <p class="card-more">Read More</p>
  </article>
  <article class="card abs" style="left:747px">
    <div class="card-img" role="img" aria-label="Foam roller exercise" style="background:linear-gradient(135deg,#e2ecf4,#9fbfd8)"></div>
    <h3 class="card-title">Sed condimentum tempus eros,</h3>
    <p class="card-date">18 November 2017</p>
    <p class="card-text">It is a long established fact that a reader will be distracted by the readable content of a page...</p>
    <p class="card-more">Read More</p>
  </article>
</section>

<section class="testimonials">
  <h2 class="section-title-dark abs">What Our Customer Saying About Us</h2>
  <p class="section-sub abs">Aliquam sagittis tellus vitae nunc ornare, eget porttitor odio malesuada.<br>Morbi magna eros, lobortis eget urna at.</p>
  <p class="section-link abs">click here to see all testimonials</p>
  <svg class="quote-nav abs" style="left:927px" viewBox="0 0 20 20"><path d="M12 6l-4 4 4 4" fill="none" stroke="#8b3f9d" stroke-width="2"/></svg>
  <svg class="quote-nav abs" style="left:949px" viewBox="0 0 20 20"><path d="M8 6l4 4-4 4" fill="none" stroke="#8b3f9d" stroke-width="2"/></svg>
  <div class="quote-box abs"></div>
  <div class="quote-photo abs"><div role="img" aria-label="Portrait of a client"></div></div>
  <p class="quote-text abs">I attended your clinic recently and was surprised. I am 68 years old and never before was I received so warmly. I believe that natural medicine is the best medicine for all of us. It has fewer and more benign side effects than those created in labs. Your clinic I dream will be the future of health care. My regret is that most patients are misled by the medical and pharmaceutical powers that be to sway their minds to traditional methods of treating their conditions. I wish all of you well in your endeavors.</p>
  <p class="quote-sign abs">Regards Milo</p>
  <div class="rating abs" style="left:210px" aria-label="Zintrel reviews badge"><svg width="120" height="50"><rect width="120" height="50" rx="6" fill="#eaeaea"/></svg></div>
  <div class="rating abs" style="left:398px" aria-label="Quorva reviews badge"><svg width="120" height="50"><rect width="120" height="50" rx="6" fill="#f1dede"/></svg></div>
  <div class="rating abs" style="left:608px" aria-label="Five star rating badge"><svg width="70" height="80"><rect x="5" y="5" width="60" height="70" rx="8" fill="#2fb3ad"/></svg></div>
  <div class="rating abs" style="left:807px" aria-label="Vetora rating badge"><svg width="120" height="50"><rect width="120" height="50" rx="6" fill="#e2eff0"/></svg></div>
</section>

<section class="cta">
  <h2 class="cta-title abs">Ready to Eliminate Your Pain?</h2>
  <p class="cta-line abs"><b>Book an Appointment</b> directly online or contact us at</p>
  <p class="cta-phone abs"><strong>555-014-2290</strong> to ask us a question.</p>
  <div class="btn-slant btn-white btn-book-alt abs">Book an Appointment</div>
  <div class="btn-slant btn-white btn-ask abs">Ask Us a Question?</div>
</section>

<footer class="site-footer">
  <div class="foot-col abs" style="left:220px"><h4>Navigation</h4><p>Home<br>Fees and Services<br>Our Staff<br>News &amp; Updates<br>Corporate Wellness<br>Forms<br>Contact</p></div>
  <div class="foot-col abs" style="left:375px"><h4>Our Services</h4><p>Chiropractic<br>Physiotherapy<br>Active Rehabilitation<br>Massage Therapy<br>Chiropody<br>Osteopathy</p></div>
  <div class="foot-col abs" style="left:545px"><h4>Hours of Operations</h4><p>Monday - Friday 7:30am - 8pm<br>Saturday 10am - 5pm<br>Sunday 10am - 5pm</p></div>
  <div class="foot-col abs" style="left:786px"><h4>Contact Us</h4><p>Thornleigh Vitality Centre<br>14 Elm Grove Lane, Suite 210<br>Toronto, Ontario<br>M4W 0A1<br>Phone: 555-014-2290<br>Fax: 555-014-2291</p></div>
  <div class="foot-rule abs"></div>
  <div class="social abs">Be social with us <span class="dot"></span><span class="dot"></span><span class="dot"></span></div>
  <div class="foot-brand abs"><span></span>Thornleigh Vitality Centre</div>
</footer>

</body>
</html>
```